BrivoLane Ute.

I want the full logo on one side. And the other side the card if right Ralf the logo the left half orange like the car in the logo color with Danielle R Morrow
Founder and CEO
Email symbol then dmorrow@brivolaneute.com
Www symbol. Then Brivolaneute.com
Phone symbol then 413-926-BRIV
The very bottom would like Brivo Lane Ute is a division of Harmond Vistas. LLC

```html
<!DOCTYPE html>
<html lang="en">
<head>
<meta charset="utf-8">
<title>Brivo Lane Ute — Business Card</title>
<link rel="stylesheet" href="https://fonts.googleapis.com/css2?family=Questrial&family=Roboto+Slab:wght@700&display=swap">
<style>
  :root{
    --bg:#2a2a2a;
    --card:#ffffff;
    --ink:#1c1c1c;
    --orange:#e98f2a;
    --sand:#efcdb2;
    --red:#e3323b;
    --white:#ffffff;
  }
  *{margin:0;padding:0;box-sizing:border-box}
  html,body{width:1200px;height:1200px;overflow:hidden;background:var(--bg)}
  .canvas{position:relative;width:1200px;height:1200px}
  .card{position:absolute;left:185px;width:850px;height:482px;background:var(--card);border-radius:26px;overflow:hidden;box-shadow:0 4px 14px rgba(0,0,0,.35)}
  .card--front{top:88px}
  .card--back{top:642px}

  .brand-name{font-family:"Roboto Slab",serif;font-weight:700;color:var(--ink);white-space:nowrap;letter-spacing:1px}
  .card--front .brand-name{position:absolute;left:0;right:0;top:180px;text-align:center;font-size:50px}
  .front-site{position:absolute;left:0;right:0;top:410px;text-align:center;font-family:"Questrial",sans-serif;font-size:20px;color:var(--ink)}

  .waves{position:absolute;left:0;top:0;width:850px;height:482px}

  .person{position:absolute;left:36px;top:42px}
  .person__name{font-family:"Roboto Slab",serif;font-weight:700;font-size:38px;line-height:1;color:var(--ink)}
  .person__name .accent{color:var(--orange)}
  .person__title{font-family:"Questrial",sans-serif;font-size:19px;color:var(--ink);margin-top:8px}

  .card--back .brand-name{position:absolute;left:450px;width:400px;top:150px;text-align:center;font-size:40px}

  .contacts{position:absolute;right:62px;top:300px;list-style:none}
  .contacts li{display:flex;align-items:center;justify-content:flex-end;height:31px;margin-bottom:11px;font-family:"Questrial",sans-serif;font-size:21px;color:var(--ink)}
  .contacts .icon{width:31px;height:31px;margin-left:17px;background:var(--orange);border-radius:6px;display:flex;align-items:center;justify-content:center}
  .contacts svg{width:19px;height:19px}

  .address{position:absolute;left:36px;top:376px;font-family:"Roboto Slab",serif;font-weight:700;font-size:18px;line-height:23px;color:var(--white)}
  .division{position:absolute;left:36px;top:448px;font-family:"Questrial",sans-serif;font-size:13px;color:var(--white);white-space:nowrap}
</style>
</head>
<body>
<main class="canvas">

  <section class="card card--front">
    <p class="brand-name">Brivo Lane Ute</p>
    <p class="front-site">brivolaneute.com</p>
  </section>

  <section class="card card--back">
    <svg class="waves" viewBox="0 0 850 482" aria-hidden="true">
      <path fill="var(--orange)" d="M0,160 C150,260 250,330 340,365 C480,420 640,468 850,472 L850,482 L0,482 Z"/>
      <path fill="var(--sand)" d="M0,91 C160,220 300,345 430,405 C560,455 700,468 850,462 L850,472 C640,468 480,420 340,365 C250,330 150,260 0,160 Z"/>
      <path fill="var(--red)" d="M330,356 C348,340 372,340 392,352 C480,410 640,462 850,452 L850,460 C640,472 470,430 330,356 Z"/>
    </svg>

    <div class="person">
      <h1 class="person__name">Danielle <span class="accent">R Morrow</span></h1>
      <p class="person__title">Founder and CEO</p>
    </div>

    <p class="brand-name">Brivo Lane Ute</p>

    <ul class="contacts">
      <li>413-926-BRIV
        <span class="icon"><svg viewBox="0 0 24 24"><path fill="#fff" d="M6.6 10.8a15.1 15.1 0 0 0 6.6 6.6l2.2-2.2c.3-.3.7-.4 1-.2 1.1.4 2.3.6 3.6.6.6 0 1 .4 1 1V20c0 .6-.4 1-1 1A17 17 0 0 1 3 4c0-.6.4-1 1-1h3.5c.6 0 1 .4 1 1 0 1.3.2 2.5.6 3.6.1.3 0 .7-.2 1z"/></svg></span>
      </li>
      <li>dmorrow@brivolaneute.com
        <span class="icon"><svg viewBox="0 0 24 24" fill="none" stroke="#fff" stroke-width="2"><rect x="3" y="5" width="18" height="14" rx="1"/><path d="M3 6l9 7 9-7"/></svg></span>
      </li>
      <li>brivolaneute.com
        <span class="icon"><svg viewBox="0 0 24 24" fill="none" stroke="#fff" stroke-width="1.8"><circle cx="12" cy="12" r="9"/><ellipse cx="12" cy="12" rx="4" ry="9"/><path d="M3 12h18M5 7h14M5 17h14"/></svg></span>
      </li>
    </ul>

    <p class="address">1200, Addres Line Here,<br>Country Name, 35555</p>
    <p class="division">Brivo Lane Ute is a division of Harmond Vistas. LLC</p>
  </section>

</main>
</body>
</html>
```